1 page A4 double sided Brochure Design Folded to envelope size. Interesting fold design would be co

Small family run guesthouse BnB in Blue Mountains Australia needs a new brochure showing different aspects of business

We need a new brochure to go with our new website. Basically the design would be good as a double sided brochure that can be folded down to standard envelope size.

We have seen a few interesting brochure designs before that fold in different ways (and therefore have the design to match) but still fold down to this size to help with postage.

The design would have to showcase the different aspects of our business including individual accommodation for couples and families, conference market, wedding market, retreat market and events market (parties, re-unions etc). The Business must be Showcased as The Fernlight Lodge, Blue Mountains

It is possible to arrange design so folds separate different sections of info/pictures.

It is also optional that we possibly have 2 brochures instead, one that is a basic all inclusive once described and one that only deals with group bookings (wedding conference retreats etc etc)

Must match design elements from our web page. Feel free to take informations, elements and images from there for design www.fernlightlodge-example.com.au

Here is a link to our view we wake up to every morning to inspire all those working on a design!
http://www.fernlightlodge-example.com.au/images/view.jpg

Target Market(s)

Group bookings, weddings, conferences, retreats, events and Blue Mountains Travellers

Industry/Entity Type

Accommodation

Requirements
Must have
• Must be based on our current websites design feel, colours, etc
Must be showcased as The Fernlight Lodge Blue Mountains.
Must mention The Blue Mountains as a world heritage destination
Must be A4 double sided that can fold down to 1/3 the size to fit into a standard envelope. Any designs that will not fit in a standard envelope once folded can not be accepted as they are outside the brief
Nice to have
• Interesting folding design to get people interested to read it.

```html
<!DOCTYPE html>
<html lang="en">
<head>
<meta charset="utf-8">
<title>The Fernlight Lodge, Blue Mountains – Brochure</title>
<link rel="stylesheet" href="https://fonts.googleapis.com/css2?family=Arimo:wght@400;700&family=Roboto+Condensed:wght@400;700&display=swap">
<style>
  :root {
    --page-bg: #ffffff;
    --charcoal: #39352f;
    --mint: #e4f4d8;
    --mint-strong: #d2ecc0;
    --text-light: #f2f0ea;
    --photo-forest: #4f6b3a;
    --photo-sky: #a9c1cf;
    --photo-grass: #7fa64a;
  }
  * { box-sizing: border-box; margin: 0; padding: 0; }
  html, body {
    width: 1200px;
    height: 994px;
    overflow: hidden;
    background: var(--page-bg);
  }
  .spread {
    position: absolute;
    top: 97px;
    left: 33px;
    display: flex;
    gap: 14px;
  }
  .panel {
    position: relative;
    width: 560px;
    height: 800px;
    background: var(--charcoal);
    overflow: hidden;
  }
  .panel-art {
    position: absolute;
    inset: 0;
    width: 560px;
    height: 800px;
  }
  .cover-headline {
    position: absolute;
    top: 74px;
    right: 36px;
    width: 430px;
    text-align: right;
    font-family: "Arimo", Arial, sans-serif;
    font-weight: 700;
    font-size: 21px;
    line-height: 1.2;
    color: var(--text-light);
  }
  .cover-headline .highlight { color: var(--mint-strong); }
  .brand-block {
    position: absolute;
    left: 30px;
    top: 652px;
    width: 122px;
    height: 148px;
    background: var(--charcoal);
  }
  .brand-square {
    width: 122px;
    height: 76px;
    background: var(--mint);
  }
  .brand-name {
    margin-top: 10px;
    text-align: center;
    font-family: "Roboto Condensed", Arial, sans-serif;
    font-size: 13px;
    line-height: 1.15;
    color: var(--text-light);
  }
  .brand-phone {
    margin-top: 4px;
    text-align: center;
    font-family: "Roboto Condensed", Arial, sans-serif;
    font-size: 12px;
    color: var(--text-light);
  }
  .info {
    position: absolute;
    left: 40px;
    top: 462px;
    width: 482px;
    font-family: "Roboto Condensed", Arial, sans-serif;
    font-size: 12.5px;
    line-height: 1.38;
    color: var(--text-light);
  }
  .info p { margin-bottom: 11px; }
  .info-rule {
    border: 0;
    border-top: 1px dashed var(--mint-strong);
    margin: 8px 0 10px;
  }
  .info-contact {
    font-family: "Arimo", Arial, sans-serif;
    font-weight: 700;
    font-size: 17px;
    color: var(--mint-strong);
  }
</style>
</head>
<body>
<main class="spread">

  <section class="panel panel-cover">
    <svg class="panel-art" viewBox="0 0 560 800" aria-hidden="false">
      <defs>
        <linearGradient id="forestTone" x1="0" y1="0" x2="0" y2="1">
          <stop offset="0" stop-color="#5c7a45"/>
          <stop offset="0.55" stop-color="var(--photo-forest)"/>
          <stop offset="1" stop-color="var(--photo-grass)"/>
        </linearGradient>
        <clipPath id="coverPhotoClip">
          <path d="M0,262 C120,250 210,300 300,360 C390,420 470,455 560,460 V800 H0 Z"/>
        </clipPath>
      </defs>
      <path class="cover-wave" d="M0,236 C120,224 215,276 305,336 C395,396 475,432 560,436 V470 C470,465 390,430 300,370 C210,310 120,262 0,274 Z" fill="var(--mint)"/>
      <rect class="cover-photo" role="img" aria-label="Photo of a bushland path leading through green scrub towards forested world heritage mountains" x="0" y="230" width="560" height="570" fill="url(#forestTone)" clip-path="url(#coverPhotoClip)"/>
    </svg>

    <h1 class="cover-headline">Family Owned and run <span class="highlight">Blue Mountains</span> accommodation, retreat, conference, wedding and function centre set on 32 acres of virgin bushland in the beauty of a world heritage location.</h1>

    <div class="brand-block">
      <div class="brand-square"></div>
      <p class="brand-name">The Fernlight Lodge</p>
      <p class="brand-phone">02 5550 1234</p>
    </div>
  </section>

  <section class="panel panel-info">
    <svg class="panel-art" viewBox="0 0 560 800">
      <rect x="0" y="0" width="560" height="800" fill="var(--mint)"/>
      <path class="info-field" d="M0,450 C130,425 270,380 410,300 C490,255 530,228 560,218 V800 H0 Z" fill="var(--charcoal)"/>
      <path class="info-corner" d="M340,0 H560 V170 C480,150 400,90 340,0 Z" fill="var(--charcoal)"/>

      <g class="photo-circles">
        <circle cx="127" cy="199" r="103" fill="var(--mint)"/>
        <circle role="img" aria-label="Photo of a dining terrace overlooking the valley" cx="127" cy="199" r="96" fill="#8a6f5c"/>

        <circle cx="338" cy="137" r="128" fill="var(--mint)"/>
        <circle role="img" aria-label="Photo of the pool and shade sails among eucalyptus trees" cx="338" cy="137" r="120" fill="#6f8f73"/>

        <circle cx="186" cy="338" r="93" fill="var(--mint)"/>
        <circle role="img" aria-label="Photo of the guesthouse building set in the garden" cx="186" cy="338" r="86" fill="#7a8a5a"/>

        <circle cx="363" cy="355" r="87" fill="var(--mint)"/>
        <circle role="img" aria-label="Photo of a guest bedroom with garden doors" cx="363" cy="355" r="80" fill="#a9826b"/>
      </g>
    </svg>

    <div class="info">
      <p>The Fernlight Lodge Blue Mountains is a small family run guesthouse, bush retreat and function centre.</p>
      <p>Located on 32 acres of pristine virgin bushland in the centre of world heritage listed national park land The Fernlight Lodge is your perfect Blue Mountains accommodation whether you are looking for a quiet place to escape with someone special or a function or conference venue in the Blue Mountains for your next group escape or private, personal, specially tailored wedding.</p>
      <p>The Fernlight Lodge has 2 buildings. The main retreat with 20 well appointed en suited rooms, each with views across the pool and valley, along with 2 function rooms, games room, commercial kitchen, pool and outdoor BBQ area. The second is our manor house, a large, simple 7 bedroom, 4 bathroom house with lounge kitchen and dining room.</p>
      <p>Together with our private, friendly, family run atmosphere The Fernlight Lodge is the perfect place to escape the real world and explore another.</p>
      <hr class="info-rule">
      <p class="info-contact">www.fernlightlodge-example.com.au • P : 02 5550 1234</p>
    </div>
  </section>

</main>
</body>
</html>
```